To create an A4 brochure for protective coatings 4 pages.
Title - CUI, High Heat and Insulative Coatings
sub title - 1K Third Generation Polysiloxane Coating (TGPS) technologies
images - Oil & Gas, Chemical and offshore
Introduction - Corrosion under insulation (CUI) is a well-known industrial problem that has been plaguing asset owners for decades. CUI represents one of the costliest corrosion factors for the oil and
gas, petrochemical and general processing industries and can
lead to unplanned shutdowns, maintenance repairs and even
explosions on live plants.
TGPS Benefits - 3rd generation polysiloxane which has been introduced for CUI mitigation purposes. Developed and launched in 2015, the new coating has been tested against multiple laboratory and field test protocols. The characteristics of this coating are that it is a one component, fully ambient-curing inorganic polysiloxane which is ceramic in nature and eliminates the field issues associated with SGPS coatings. With the elimination of the heating step that was previously required for SGPS, full protection is conferred upon application at ambient temperatures as low as 1 °C and across a specified operating range of -196 to 650 °C, without the need for heating to develop the properties required for CUI protection.
Insulation Coatings - Our third-generation
polysiloxane insulative coating is a water-borne (low-VOC) one-component, ambient-curing polysiloxane TIC coating. It is designed for ultra-highbuild (UHB) in excess of 20,000 µm dry film thickness (DFT) and a temperature tolerance range from -60 to 400 °C which exceeds the current 180 °C limitation of thermal insulation coatings. The polysiloxane TIC coating can be applied over a TGPS CUI primer as a system for high temperature exposure, personnel protection and thermal insulation
purposes.
Products:
Ovanthe KR 310
Ovanthe KR 640
Ovanthe SP 620
Calorex TIP 350 - inorganic, ambient curing 1K coating designed for colour permanent changing to white for identification or 'hot spots'.
Ovanthe HT 1150
Ovanthe IL 190
Ovanthe IL 410
for other products information please see attached brochure.
use good clear images of markets sectors (oil&gas, Telecoms, Industrial)
use icons for low VOC, low toxicity, CUI mitigation, chemical resistance, maintenance friendly, environment friendly, non-isocyanate.

Company Info
Tel +44 (0) 1632 960418
Email sales@kl-dn.com
Address 7-8 Wellbrook Meadow Business Park, Fennick Lane, United Kingdom
web www.kl-dn.com

```html
<!DOCTYPE html>
<html lang="en">
<head>
<meta charset="UTF-8">
<title>Ovanthe Products</title>
<link rel="stylesheet" href="https://fonts.googleapis.com/css2?family=Poppins:wght@600;700&display=swap">
<style>
  :root {
    --navy: #1f3f87;
    --navy-deep: #1a3878;
    --navy-light: #2d56a4;
    --sky: #5aaedc;
    --white: #ffffff;
  }
  html, body {
    margin: 0;
    padding: 0;
    overflow: hidden;
    background: var(--white);
  }
  .page {
    position: relative;
    width: 848px;
    height: 1200px;
    overflow: hidden;
    background: var(--white);
    font-family: "Poppins", Arial, sans-serif;
  }
  .decor {
    position: absolute;
    inset: 0;
  }
  .section-tab {
    position: absolute;
    left: 0;
    top: 134px;
    width: 264px;
    height: 61px;
    background: var(--sky);
    border-radius: 0 31px 31px 0;
    color: var(--white);
    font-weight: 700;
    font-size: 28px;
    line-height: 61px;
    padding-left: 47px;
    box-sizing: border-box;
  }
  .product-name {
    position: absolute;
    height: 66px;
    background: var(--navy);
    color: var(--white);
    font-weight: 600;
    font-size: 24px;
    line-height: 66px;
    white-space: nowrap;
    box-sizing: border-box;
  }
  .product-name.right-photo {
    left: 228px;
    width: 380px;
    border-radius: 33px 0 0 33px;
    padding-left: 30px;
  }
  .product-name.left-photo {
    left: 240px;
    width: 370px;
    border-radius: 0 33px 33px 0;
    padding-left: 66px;
  }
  .product-photo {
    position: absolute;
    width: 228px;
    height: 228px;
    border-radius: 50%;
    border: 6px solid var(--sky);
    box-sizing: border-box;
    background: var(--white);
  }
  .product-photo .fill {
    position: absolute;
    inset: 4px;
    border-radius: 50%;
  }
  .photo-vessel .fill { background: linear-gradient(180deg, #6f9fd6 0%, #8d9290 45%, #5d6360 75%, #3c3e3e 100%); }
  .photo-tank .fill { background: linear-gradient(160deg, #bfc3c4 0%, #dcdedb 45%, #9ea3a3 100%); }
  .photo-pipework .fill { background: linear-gradient(180deg, #9aa19c 0%, #c9cdc9 45%, #dfe2e1 75%, #bdbfb8 100%); }
  .photo-plant .fill { background: linear-gradient(150deg, #3e6fae 0%, #7b8a96 45%, #5f6c74 75%, #3c4650 100%); }
  .photo-storage .fill { background: linear-gradient(180deg, #2b86d9 0%, #5aa6ea 45%, #eef1f2 65%, #7a9b55 100%); }
  .photo-supports .fill { background: linear-gradient(160deg, #cfd1d2 0%, #9fa3a5 50%, #7c8082 100%); }
</style>
</head>
<body>
<main class="page">
  <svg class="decor" width="848" height="1200" viewBox="0 0 848 1200" aria-hidden="true">
    <ellipse cx="470" cy="-70" rx="330" ry="190" fill="var(--navy-light)"/>
    <ellipse cx="435" cy="-85" rx="340" ry="210" fill="var(--navy-deep)"/>
    <circle cx="900" cy="1330" r="300" fill="var(--sky)"/>
  </svg>

  <div class="section-tab">Products</div>

  <div class="product-name right-photo" style="top:248px">Ovanthe KR 640</div>
  <div class="product-photo photo-vessel" style="left:556px; top:167px">
    <div class="fill" role="img" aria-label="Large coated pressure vessel on a heavy transport trailer"></div>
  </div>

  <div class="product-photo photo-tank" style="left:46px; top:316px">
    <div class="fill" role="img" aria-label="Long white coated horizontal vessel in a workshop"></div>
  </div>
  <div class="product-name left-photo" style="top:405px">Ovanthe KR 310</div>

  <div class="product-name right-photo" style="top:563px">Ovanthe IL 410</div>
  <div class="product-photo photo-pipework" style="left:556px; top:470px">
    <div class="fill" role="img" aria-label="Grey insulative coating on plant pipework and equipment"></div>
  </div>

  <div class="product-photo photo-plant" style="left:46px; top:627px">
    <div class="fill" role="img" aria-label="Industrial plant structure with blue column and pipe racks"></div>
  </div>
  <div class="product-name left-photo" style="top:716px">Ovanthe HT 1150</div>

  <div class="product-name right-photo" style="top:875px">Ovanthe IL 190</div>
  <div class="product-photo photo-storage" style="left:556px; top:784px">
    <div class="fill" role="img" aria-label="White storage tank under a blue sky"></div>
  </div>

  <div class="product-photo photo-supports" style="left:46px; top:938px">
    <div class="fill" role="img" aria-label="Rows of coated steel pipe support clamps"></div>
  </div>
  <div class="product-name left-photo" style="top:1025px">Ovanthe SP 620</div>
</main>
</body>
</html>
```